Business card New design- upscale

Looking for modern design business cards. Minimalist, mix of gloss and matte finishes. Texas based Contractor company doing Mechanical hvac and plumbing, focused on commercial and industrial manufacturing facilities. We don't hand too many out so high end materials or functionality...will be considered. Please see attached files for info needed on cards. *New plumbing license needs to be edited to say M82716. Www.polvaxgroup.com
P.s. Website will also be redesigned soon.

Target Market(s)

Facility managers for commercial buildings, mechanical engineers for industrial manufacturing facilities including pharmaceutical, semiconductor, food & beverage, etc

Contact Information for Business Card

See attached images

Requirements
Must have
• All Logo colors: purple, black and Gray. 1, 2 or 4 rounded corners. All content on existing business cards (see attached images).
Nice to have
• Matte and gloss print. Embossing, raised print, functionality.
Should not have
• Stock images, generic construction.

```html
<!DOCTYPE html>
<html lang="en">
<head>
<meta charset="utf-8">
<title>Polvax Group business card</title>
<link rel="stylesheet" href="https://fonts.googleapis.com/css2?family=Roboto:wght@400;500;700&display=swap">
<style>
  :root{
    --page:#e9e7ec;
    --purple-deep:#34205f;
    --purple:#3f2674;
    --mark:#4b2f86;
    --ink:#ffffff;
  }
  *{box-sizing:border-box;margin:0;padding:0}
  html,body{width:1200px;height:881px;overflow:hidden;background:var(--page)}
  body{font-family:"Roboto",Arial,sans-serif;color:var(--ink)}
  .sheet{position:relative;width:1200px;height:881px}
  .card{
    position:absolute;top:60px;width:434px;height:760px;border-radius:34px;
    background:
      linear-gradient(118deg, transparent 44%, rgba(255,255,255,.10) 52%, rgba(255,255,255,.04) 60%, transparent 66%),
      linear-gradient(180deg, var(--purple) 0%, var(--purple-deep) 100%);
    box-shadow:0 10px 30px rgba(40,20,70,.25);
    overflow:hidden;
  }
  .card--back{left:120px}
  .card--front{left:646px}
  .brand{
    position:absolute;top:58px;right:44px;
    display:flex;align-items:flex-start;gap:12px;
    font-weight:500;font-size:42px;letter-spacing:2px;color:var(--mark);
    text-transform:uppercase;line-height:1;
  }
  .brand-box{flex:none;width:22px;height:22px;border:3px solid var(--mark);margin-top:10px}
  .brand-name{display:block}
  .regulatory{
    position:absolute;top:220px;left:20px;right:20px;text-align:center;
    font-size:22px;line-height:33px;font-weight:400;
  }
  .contact{position:absolute;left:52px;right:40px;bottom:46px}
  .person{font-size:40px;font-weight:700;letter-spacing:.5px;text-transform:uppercase}
  .role{font-size:20px;margin-top:4px}
  .icons{display:flex;gap:8px;margin:18px 0 12px}
  .icons svg{width:24px;height:24px}
  .line{font-size:21px;line-height:31px}
  .rule{height:2px;background:var(--ink);width:300px;margin:14px 0 12px}
  .services{font-size:21px;line-height:31px}
</style>
</head>
<body>
<main class="sheet">
  <section class="card card--back" aria-label="Card back">
    <div class="brand"><span class="brand-box"></span><span class="brand-name">Polvax<br>Group</span></div>
    <p class="regulatory">
      M-82716 Regulated by<br>the Calder State Board of<br>Pipefitting Examiners,<br>P.O. Box 4410,<br>Austin, TX. 78760;<br>1-800-555-0162,<br>512-555-0127 /<br>TACLA30518B<br>Regulated by the Calder<br>Department of Trades and<br>Certification, P.O. Box 12930,<br>Austin, TX. 78714;<br>1-800-555-0175,<br>512-555-0139<br>www.tradelicense-tx.org
    </p>
  </section>

  <section class="card card--front" aria-label="Card front">
    <div class="brand"><span class="brand-box"></span><span class="brand-name">Polvax<br>Group</span></div>
    <div class="contact">
      <h1 class="person">Dale Morrow</h1>
      <p class="role">Lead Estimator/Sr. Project Manager</p>
      <div class="icons" aria-hidden="true">
        <svg viewBox="0 0 24 24"><circle cx="12" cy="12" r="11" fill="none" stroke="#fff" stroke-width="1.4"/><rect x="9" y="6" width="6" height="12" rx="1" fill="none" stroke="#fff" stroke-width="1.4"/></svg>
        <svg viewBox="0 0 24 24"><circle cx="12" cy="12" r="11" fill="none" stroke="#fff" stroke-width="1.4"/><path d="M8 7c0 5 4 9 9 9l1-2-3-1-1 1c-2-1-3-2-4-4l1-1-1-3z" fill="none" stroke="#fff" stroke-width="1.3"/></svg>
        <svg viewBox="0 0 24 24"><circle cx="12" cy="12" r="11" fill="none" stroke="#fff" stroke-width="1.4"/><rect x="7" y="8" width="10" height="8" fill="none" stroke="#fff" stroke-width="1.3"/><path d="M7 8l5 4 5-4" fill="none" stroke="#fff" stroke-width="1.3"/></svg>
        <svg viewBox="0 0 24 24"><circle cx="12" cy="12" r="11" fill="none" stroke="#fff" stroke-width="1.4"/><circle cx="12" cy="12" r="6" fill="none" stroke="#fff" stroke-width="1.2"/><path d="M6 12h12M12 6c-3 3-3 9 0 12M12 6c3 3 3 9 0 12" fill="none" stroke="#fff" stroke-width="1.1"/></svg>
      </div>
      <p class="line">(520) 555-0148</p>
      <p class="line">(817) 555-0193</p>
      <p class="line">dmorrow@polvaxgroup.com</p>
      <p class="line">www.polvaxgroup.com</p>
      <div class="rule"></div>
      <p class="services">Commercial &amp; Industrial Contractors<br>Mechanical &amp; Plumbing Services</p>
    </div>
  </section>
</main>
</body>
</html>
```